Our Company name is Bluefield Office Cleaning Services. We are a Toronto(GTA) company looking for a brochure that with Logo design that gives a description of what we do.

We are a company that specializes in cleaning and sanitizing office/ workplaces. Our Experience includes working with school boards and hospitals, and have 15 plus years experience. We are looking for a simple design that catches and explains to our customers what we offer with some pics, which you can provide.

if you have any questions please let us know.

thank you

Target Market(s)

We are focusing Businesses

Font styles to use
Serif

Colors

Designer to choose colors to be used in the design.

Requirements
Must have
• Must have our name/Logo, brief description of what we do. Contact numbers, (416)-555-0183/ (647)555-0927 email (bluefieldofficecleaningservices@mailbox-example.com
• Pics which you can provide
Nice to have
• We trust your imagination on this

```html
<!DOCTYPE html>
<html lang="en">
<head>
<meta charset="utf-8">
<title>Bluefield Office Cleaning Services – Brochure</title>
<link rel="stylesheet" href="https://fonts.googleapis.com/css2?family=EB+Garamond:wght@400;500&family=Libre+Baskerville:wght@700&display=swap">
<style>
  :root {
    --white: #ffffff;
    --ink: #1a1a1a;
    --navy: #1f3f8f;
    --hero-top: #7d7fcb;
    --hero-bottom: #3a8d9f;
    --band-teal: #2c8f98;
    --band-blue: #0f5cab;
    --photo-light: #eef0ec;
    --photo-mid: #c9cfc6;
    --photo-dark: #3f6450;
  }
  * { margin: 0; padding: 0; box-sizing: border-box; }
  html, body { width: 848px; height: 1200px; overflow: hidden; background: var(--white); }
  .brochure { position: relative; width: 848px; height: 1200px; overflow: hidden; font-family: "EB Garamond", serif; }

  .hero-team {
    position: absolute; left: 0; top: 0; width: 400px; height: 668px;
    background: linear-gradient(180deg, var(--hero-top) 0%, #5f8fc0 45%, var(--hero-bottom) 100%);
  }
  .hero-cleaner {
    position: absolute; left: 400px; top: 0; width: 448px; height: 668px;
    background: linear-gradient(160deg, var(--photo-light) 0%, var(--photo-mid) 45%, var(--photo-dark) 100%);
  }

  .brand-mark { position: absolute; left: 0; width: 400px; top: 108px; text-align: center; color: var(--white); font-family: "Libre Baskerville", serif; font-weight: 700; }
  .brand-mark .brand-name { font-size: 30px; letter-spacing: 1px; line-height: 1; }
  .brand-mark .brand-sub { font-size: 8.5px; letter-spacing: 2.2px; margin-top: 8px; }

  .service { position: absolute; text-align: center; color: var(--white); font-family: "Libre Baskerville", serif; font-weight: 700; font-size: 18px; width: 180px; }
  .service svg { display: block; margin: 0 auto 6px; }
  .service--cleaning { left: 10px; top: 236px; }
  .service--sanitation { left: 195px; top: 236px; }
  .service--trust { left: 110px; top: 386px; }

  .info-band {
    position: absolute; left: 0; top: 668px; width: 848px; height: 532px;
    background: linear-gradient(135deg, var(--band-teal) 0%, #1a76a6 45%, var(--band-blue) 100%);
  }

  .about { position: absolute; left: 19px; top: 730px; width: 358px; color: var(--white); }
  .about h2 { font-family: "Libre Baskerville", serif; font-weight: 700; font-size: 24px; margin-left: 26px; margin-bottom: 18px; letter-spacing: 0.2px; }
  .about p { font-size: 17px; line-height: 34.4px; text-align: justify; }

  .contact { position: absolute; left: 37px; color: var(--white); font-size: 16.5px; line-height: 21px; display: flex; align-items: center; gap: 14px; }
  .contact--phone { top: 1063px; }
  .contact--email { top: 1114px; width: 350px; }
  .contact--email .email-address { flex: 1; min-width: 0; }

  .details-panel { position: absolute; left: 400px; top: 682px; width: 448px; height: 502px; background: var(--white); }
  .details-panel .panel-brand { text-align: center; margin-top: 40px; color: var(--navy); font-family: "Libre Baskerville", serif; font-weight: 700; }
  .details-panel .panel-brand .brand-name { font-size: 30px; letter-spacing: 1px; line-height: 1; }
  .details-panel .panel-brand .brand-sub { font-size: 8.5px; letter-spacing: 2.2px; margin-top: 8px; }
  .details-panel p { position: absolute; left: 10px; top: 132px; width: 422px; color: var(--ink); font-size: 20.5px; line-height: 24px; text-align: justify; }
</style>
</head>
<body>
<div class="brochure">
  <div class="hero-team" role="img" aria-label="Photo of a cleaning team mopping and wiping in an office, under a blue-violet tint"></div>
  <div class="hero-cleaner" role="img" aria-label="Photo of a smiling cleaner in green overalls and yellow gloves holding a spray bottle and cloth"></div>

  <div class="brand-mark">
    <div class="brand-name">BLUEFIELD</div>
    <div class="brand-sub">OFFICE CLEANING SERVICES</div>
  </div>

  <div class="service service--cleaning">
    <svg width="100" height="100" viewBox="0 0 100 100" fill="none" stroke="#fff" stroke-width="4" stroke-linecap="round" stroke-linejoin="round">
      <line x1="10" y1="10" x2="50" y2="50"/>
      <path d="M42 56 L58 40 L80 70 L72 78 Z"/>
      <path d="M72 82 q4 -4 0 -8 q-4 -4 0 -8"/>
      <path d="M82 84 q4 -4 0 -8 q-4 -4 0 -8"/>
      <path d="M92 84 q4 -4 0 -8 q-4 -4 0 -8"/>
    </svg>
    <span>CLEANING</span>
  </div>

  <div class="service service--sanitation">
    <svg width="100" height="100" viewBox="0 0 100 100" fill="none" stroke="#fff" stroke-width="4" stroke-linejoin="round">
      <path d="M30 8 H58 V18"/>
      <rect x="44" y="18" width="14" height="10"/>
      <rect x="30" y="28" width="42" height="68" rx="4"/>
      <circle cx="51" cy="62" r="12"/>
      <path d="M51 55 V69 M44 62 H58"/>
      <line x1="30" y1="84" x2="72" y2="84"/>
    </svg>
    <span>SANITATION</span>
  </div>

  <div class="service service--trust">
    <svg width="120" height="102" viewBox="0 0 120 102" fill="none" stroke="#fff" stroke-width="4" stroke-linejoin="round">
      <rect x="22" y="48" width="20" height="50"/>
      <path d="M42 52 L62 22 Q66 4 72 6 Q80 10 76 36 H102 Q110 38 106 48 Q112 52 106 60 Q112 66 104 72 Q110 80 100 86 Q100 96 90 96 H42"/>
    </svg>
    <span>TRUSTABLE</span>
  </div>

  <div class="info-band"></div>

  <section class="about">
    <h2>ABOUT OUR COMPANY</h2>
    <p>We are a company that specializes in cleaning and sanitizing office/ workplaces. Our Experience includes working with school boards and hospitals, and have 15 plus years experience. We are looking for a simple design that catches and explains to our customers what we offer with some pics, which you can provide.</p>
  </section>

  <div class="contact contact--phone">
    <svg width="30" height="30" viewBox="0 0 24 24" fill="#fff">
      <path d="M6.6 10.8c1.4 2.8 3.8 5.1 6.6 6.6l2.2-2.2c.3-.3.7-.4 1-.2 1.1.4 2.3.6 3.6.6.6 0 1 .4 1 1V20c0 .6-.4 1-1 1C10.6 21 3 13.4 3 4c0-.6.4-1 1-1h3.5c.6 0 1 .4 1 1 0 1.3.2 2.5.6 3.6.1.3 0 .7-.2 1z"/>
      <path d="M14 3a7 7 0 0 1 7 7" fill="none" stroke="#fff" stroke-width="1.6"/>
      <path d="M14 6.5a3.5 3.5 0 0 1 3.5 3.5" fill="none" stroke="#fff" stroke-width="1.6"/>
    </svg>
    <div>(416)-555-0183<br>(647)555-0927</div>
  </div>

  <div class="contact contact--email">
    <svg width="34" height="26" viewBox="0 0 34 26" fill="#fff">
      <path d="M0 0 H34 L17 14 Z"/>
      <path d="M0 4 L12 14 L0 26 Z M34 4 L22 14 L34 26 Z M14 16 L17 18.5 L20 16 L31 26 H3 Z"/>
    </svg>
    <div class="email-address">bluefieldofficecleaningservices<wbr>@mailbox-example.com</div>
  </div>

  <section class="details-panel">
    <div class="panel-brand">
      <div class="brand-name">BLUEFIELD</div>
      <div class="brand-sub">OFFICE CLEANING SERVICES</div>
    </div>
    <p>Lorem ipsum dolor sit amet, consectetuer adipiscing elit, sed diam nonummy nibh euismod tincidunt ut laoreet dolore magna aliquam erat volutpat. Ut wisi enim ad minim veniam, quis nostrud exerci tation ullamcorper suscipit lobortis nisl ut aliquip ex ea commodo consequat. Duis autem vel eum iriure dolor in hendrerit in vulputate velit esse molestie consequat, vel illum dolore eu feugiat nulla facilisis at vero eros et accumsan et iusto odio dignissim qui blandit praesent luptatum zzril delenit augue duis dolore te feugait nullaDuis autem vel eum iriure dolor in hendrerit in vulputate velit esse molestie consequat, vel illum dolore eu feugiat nulla facilisis at vero.</p>
  </section>
</div>
</body>
</html>
```